out of the box Business Card Design for a Manufacturer / Distributor

We are a manufarturer and distributor of products.
the company name is VORTANI (Pic attached)

the picture is NOT a must have on the business Card.

the Business Card should look really professional and/or special, so out of the box thinking is welcome.

there should be 2 Adresses on the Business Card for Main and Branch Office.
Email Adress, homepage, Name is required
NO Phone Number

Our working field:
Private Labeling
high Quality Production
direct distribution
warehousing
trademark registration
legal support

Main Office:
Kornblumenweg 14
08352 Eichenfeld
Nordavia

Branch Office:
Daska Lane
Kelvara
Sundara

Names:
Lukas Feldhaus (Owner)
Imran Qureshi (Owner)

Email:
lukas@vortani-example.com
imran@vortani-example.com

homepage:
vortani-example.com

Industry/Entity Type

Manufacturer Distributer

Contact Information for Business Card

Vortani

Requirements
Must have
• Names, both office Adresses, email, homepage
Should not have
• Phone Number

```html
<!DOCTYPE html>
<html lang="en">
<head>
<meta charset="utf-8">
<title>Vortani Business Cards</title>
<link href="https://fonts.googleapis.com/css2?family=Outfit:wght@300;400;500;700&display=swap" rel="stylesheet">
<style>
  :root {
    --page: #ffffff;
    --card: #38383a;
    --card-faint: #414143;
    --ink: #ffffff;
    --muted: #8e8e90;
  }
  * { box-sizing: border-box; margin: 0; padding: 0; }
  html, body { width: 1200px; height: 1200px; overflow: hidden; background: var(--page); }
  body { position: relative; font-family: "Outfit", sans-serif; color: var(--ink); }

  .card {
    position: absolute;
    left: 294px;
    width: 620px;
    height: 372px;
    background: var(--card);
    overflow: hidden;
  }
  .card--front { top: 21px; }
  .card--back-one { top: 418px; }
  .card--back-two { top: 815px; }

  /* front */
  .frame-band {
    position: absolute;
    left: 21px; top: 21px;
    width: 578px; height: 330px;
    background: var(--card-faint);
  }
  .frame-inner {
    position: absolute;
    left: 79px; top: 81px;
    width: 460px; height: 210px;
    background: var(--card);
  }
  .front-brand {
    position: absolute;
    left: 0; right: 0; top: 140px;
    display: flex; align-items: center; justify-content: center; gap: 18px;
  }
  .brand-dot { width: 62px; height: 62px; border-radius: 50%; background: var(--ink); }
  .front-brand .brand-name { font-size: 72px; font-weight: 400; line-height: 1; letter-spacing: -0.5px; }

  /* back */
  .back-mark {
    position: absolute;
    left: 102px; top: 82px;
    width: 110px; height: 110px;
    border-radius: 50%;
    background: var(--ink);
  }
  .back-brand {
    position: absolute;
    left: 40px; top: 210px;
    width: 234px;
    font-size: 46px; font-weight: 400; line-height: 1;
    letter-spacing: -0.5px;
    text-align: center;
    white-space: nowrap;
  }
  .back-site {
    position: absolute;
    left: 30px; top: 266px;
    width: 254px;
    font-size: 15px; font-weight: 500;
    letter-spacing: 0.6px;
    text-align: center;
    white-space: nowrap;
  }
  .divider-strip {
    position: absolute;
    left: 270px; top: 114px;
    width: 15px; height: 138px;
    border-radius: 8px;
    background: var(--muted);
  }

  .contact { position: absolute; left: 304px; top: 74px; width: 300px; }
  .person-name { font-size: 26px; font-weight: 700; letter-spacing: 0.6px; line-height: 1.1; margin-left: 40px; white-space: nowrap; }
  .person-role { font-size: 21px; font-weight: 300; letter-spacing: 0.8px; line-height: 1.2; margin-left: 40px; }
  .contact-row { display: flex; align-items: flex-start; gap: 10px; margin-top: 12px; }
  .contact-row:first-of-type { margin-top: 16px; }
  .contact-icon { flex: 0 0 30px; width: 30px; height: 30px; margin-top: 1px; }
  .contact-text { font-size: 19px; font-weight: 300; line-height: 26px; letter-spacing: 0.2px; white-space: nowrap; }
  .contact-text .indent { padding-left: 5px; }
</style>
</head>
<body>

  <section class="card card--front">
    <div class="frame-band" role="img" aria-label="Faint decorative frame pattern"></div>
    <div class="frame-inner"></div>
    <div class="front-brand">
      <span class="brand-dot"></span>
      <span class="brand-name">VORTANI</span>
    </div>
  </section>

  <section class="card card--back-one">
    <div class="back-mark"></div>
    <div class="back-brand">VORTANI</div>
    <div class="back-site">www.vortani-example.com</div>
    <div class="divider-strip" role="img" aria-label="Decorative vertical chain ornament"></div>
    <div class="contact">
      <div class="person-name">Lukas Feldhaus</div>
      <div class="person-role">Owner</div>
      <div class="contact-row">
        <svg class="contact-icon" viewBox="0 0 30 30" aria-hidden="true"><circle cx="15" cy="15" r="14" fill="#fff"/><rect x="8" y="10" width="14" height="10" fill="none" stroke="#38383a" stroke-width="1.8"/><path d="M8 10 L15 16 L22 10" fill="none" stroke="#38383a" stroke-width="1.8"/></svg>
        <div class="contact-text">lukas@vortani-example.com</div>
      </div>
      <div class="contact-row">
        <svg class="contact-icon" viewBox="0 0 30 30" aria-hidden="true"><circle cx="15" cy="15" r="14" fill="#fff"/><path d="M7 14 L15 7 L23 14 Z" fill="#38383a"/><rect x="9" y="15" width="12" height="8" fill="#38383a"/></svg>
        <div class="contact-text">Kornblumenweg 14 08352<br>Eichenfeld Nordavia</div>
      </div>
      <div class="contact-row">
        <svg class="contact-icon" viewBox="0 0 30 30" aria-hidden="true"><circle cx="15" cy="15" r="14" fill="#fff"/><path d="M7 14 L15 7 L23 14 Z" fill="#38383a"/><rect x="9" y="15" width="12" height="8" fill="#38383a"/></svg>
        <div class="contact-text">Daska Lane, Kelvara,<br><span class="indent">Sundara</span></div>
      </div>
    </div>
  </section>

  <section class="card card--back-two">
    <div class="back-mark"></div>
    <div class="back-brand">VORTANI</div>
    <div class="back-site">www.vortani-example.com</div>
    <div class="divider-strip" role="img" aria-label="Decorative vertical chain ornament"></div>
    <div class="contact">
      <div class="person-name">Imran Qureshi</div>
      <div class="person-role">Owner</div>
      <div class="contact-row">
        <svg class="contact-icon" viewBox="0 0 30 30" aria-hidden="true"><circle cx="15" cy="15" r="14" fill="#fff"/><rect x="8" y="10" width="14" height="10" fill="none" stroke="#38383a" stroke-width="1.8"/><path d="M8 10 L15 16 L22 10" fill="none" stroke="#38383a" stroke-width="1.8"/></svg>
        <div class="contact-text">imran@vortani-example.com</div>
      </div>
      <div class="contact-row">
        <svg class="contact-icon" viewBox="0 0 30 30" aria-hidden="true"><circle cx="15" cy="15" r="14" fill="#fff"/><path d="M7 14 L15 7 L23 14 Z" fill="#38383a"/><rect x="9" y="15" width="12" height="8" fill="#38383a"/></svg>
        <div class="contact-text">Kornblumenweg 14 08352<br>Eichenfeld Nordavia</div>
      </div>
      <div class="contact-row">
        <svg class="contact-icon" viewBox="0 0 30 30" aria-hidden="true"><circle cx="15" cy="15" r="14" fill="#fff"/><path d="M7 14 L15 7 L23 14 Z" fill="#38383a"/><rect x="9" y="15" width="12" height="8" fill="#38383a"/></svg>
        <div class="contact-text">Daska Lane, Kelvara,<br><span class="indent">Sundara</span></div>
      </div>
    </div>
  </section>

</body>
</html>
```